Modern Logo for Law Firm
TORVE LAW FIRM
Project: Modern Logo for Law Firm
Modern Logo for Law Firm - Law
Creative Brief
Professional
Lucian Pertovalli, Esq.
Attorney at Law
3817 Carmody Ave., Suite 200 Beverly Hills, CA 90212
lp@torvelawfirm.example
www.torvelawfirm.example
We are open to all types of creative fonts...
We would prefer to have only our logo on the back with maybe our web address

```html
<!DOCTYPE html>
<html lang="en">
<head>
<meta charset="utf-8">
<title>Torve Law Firm – Business Card</title>
<link href="https://fonts.googleapis.com/css2?family=Lato:wght@400;700;900&display=swap" rel="stylesheet">
<style>
  :root {
    --bg: #e9e6e1;
    --card: #ffffff;
    --navy: #1f3f82;
    --navy-deep: #15306a;
    --orange: #f26a21;
    --amber: #fbb829;
    --ink: #1c1c1c;
    --muted: #555b66;
    --on-blue: #ffffff;
  }
  * { margin: 0; padding: 0; box-sizing: border-box; }
  html, body { width: 1200px; height: 914px; overflow: hidden; }
  body {
    background: var(--bg);
    font-family: "Lato", Arial, sans-serif;
    display: flex;
    flex-direction: column;
    align-items: center;
    justify-content: center;
    gap: 40px;
  }
  .card {
    position: relative;
    width: 700px;
    height: 400px;
    background: var(--card);
    box-shadow: 0 6px 18px rgba(0,0,0,0.18);
    overflow: hidden;
  }
  .card-art { position: absolute; inset: 0; }

  .wordmark { display: flex; align-items: center; gap: 12px; }
  .wordmark-square { width: 34px; height: 34px; background: var(--navy); }
  .wordmark-name {
    font-weight: 900;
    font-size: 34px;
    letter-spacing: 2px;
    color: var(--navy);
    line-height: 1;
  }
  .tagline {
    font-size: 10px;
    letter-spacing: 2px;
    color: var(--muted);
    margin-top: 6px;
    margin-left: 46px;
  }

  .front .brand { position: absolute; left: 36px; top: 52px; }
  .front .person { position: absolute; left: 36px; top: 196px; }
  .person-name { font-weight: 700; font-size: 19px; color: var(--ink); }
  .person-title { font-size: 13px; color: var(--muted); margin-top: 3px; }

  .address {
    position: absolute; left: 36px; top: 290px;
    color: var(--on-blue); font-size: 14px; line-height: 1.55;
  }
  .contacts {
    position: absolute; left: 400px; top: 250px;
    color: var(--on-blue); font-size: 14px; line-height: 1.7;
    display: grid; grid-template-columns: 56px auto; column-gap: 6px;
  }

  .back .brand {
    position: absolute; left: 50%; top: 150px;
    transform: translateX(-50%);
  }
  .back .wordmark-square { width: 44px; height: 44px; }
  .back .wordmark-name { font-size: 46px; }
  .back .tagline { margin-left: 56px; font-size: 12px; }
  .back-rule {
    position: absolute; left: 0; right: 0; bottom: 62px;
    height: 4px; background: var(--navy);
  }
  .back-band {
    position: absolute; left: 0; right: 0; bottom: 18px; height: 36px;
    background: var(--navy);
    color: var(--on-blue);
    font-size: 14px; letter-spacing: 3px;
    display: flex; align-items: center; justify-content: flex-end;
    padding-right: 40px;
  }
</style>
</head>
<body>

  <section class="card front">
    <svg class="card-art" width="700" height="400" viewBox="0 0 700 400" aria-hidden="true">
      <defs>
        <linearGradient id="cornerGlow" x1="0" y1="0" x2="1" y2="1">
          <stop offset="0" stop-color="#fbb829"/>
          <stop offset="1" stop-color="#f26a21"/>
        </linearGradient>
        <linearGradient id="panelBlue" x1="0" y1="0" x2="0" y2="1">
          <stop offset="0" stop-color="#2a4f98"/>
          <stop offset="1" stop-color="#15306a"/>
        </linearGradient>
      </defs>
      <rect width="700" height="400" fill="url(#panelBlue)"/>
      <polygon points="0,0 470,0 310,255 0,255" fill="#ffffff"/>
      <polygon points="470,0 492,0 332,255 310,255" fill="#f26a21"/>
      <polygon points="560,0 700,0 700,110" fill="url(#cornerGlow)"/>
      <rect x="0" y="255" width="310" height="3" fill="#f26a21"/>
    </svg>

    <div class="brand">
      <div class="wordmark">
        <span class="wordmark-square"></span>
        <span class="wordmark-name">TORVE LAW FIRM</span>
      </div>
      <div class="tagline">A PROFESSIONAL LAW CORPORATION</div>
    </div>

    <div class="person">
      <div class="person-name">Lucian Pertovalli, Esq.</div>
      <div class="person-title">Attorney at Law</div>
    </div>

    <div class="address">
      3817 Carmody Ave., Suite 200<br>
      Beverly Hills,<br>
      CA 90212
    </div>

    <div class="contacts">
      <span>Phone</span><span>: 310-555-0142</span>
      <span>Fax</span><span>: 310-555-0187</span>
      <span>Email</span><span>: lp@torvelawfirm.example</span>
    </div>
  </section>

  <section class="card back">
    <div class="brand">
      <div class="wordmark">
        <span class="wordmark-square"></span>
        <span class="wordmark-name">TORVE LAW FIRM</span>
      </div>
      <div class="tagline">A PROFESSIONAL LAW CORPORATION</div>
    </div>
    <div class="back-rule"></div>
    <div class="back-band">www.torvelawfirm.example</div>
  </section>

</body>
</html>
```